Professional Modern Website Design

We are a premium IT services provider to the financial industry based in London. Our company is called Veltra our current holding page is www.veltra-example.co.uk. We require a new website to match our new corporate identity. This project is for the design phase only. Development will be handled in-house. I have attached examples of wire frames we have developed (although open to suggestions for improvement) Our brand document that should demonstrate current brand, inc how we communicate to potential clients and finally mostly completed web-content.
We are looking for designers that can create something that sets us apart from our competitors.
Target Market(s)
IT Decision makers in Finance companies such as; hedge funds, private investment banks etc
Industry/Entity Type
Financial
Number of Pages Required
5+ page
Requirements
Must have
- hexagon elements in the design, unique design.
Nice to have
- Blog and social media feeds
Should not have
- Should not resemble a downloaded template

```html
<!DOCTYPE html>
<html lang="en">
<head>
<meta charset="utf-8">
<title>Veltra — IT Integration for Finance</title>
<link rel="stylesheet" href="https://fonts.googleapis.com/css2?family=Open+Sans:wght@400;600;700;800&display=swap">
<style>
:root{
  --orange:#f47b20;
  --orange-deep:#e2581a;
  --ink:#2b2b2b;
  --text:#555;
  --white:#fff;
  --footer:#1f1f1f;
  --footer-base:#161616;
  --footer-line:#3a3a3a;
  --nav:rgba(40,40,40,.85);
}
*{box-sizing:border-box;margin:0;padding:0}
html,body{width:700px;height:1200px;overflow:hidden}
body{position:relative;background:var(--white);font-family:"Open Sans",Arial,sans-serif;color:var(--text)}

.hero-photo{position:absolute;left:0;top:0;width:700px;height:465px;
  clip-path:polygon(0 0,700px 0,700px 400px,243px 465px,0 325px);
  background:
    linear-gradient(180deg,rgba(255,255,255,0) 58%,rgba(255,255,255,.45) 82%,rgba(255,255,255,.85) 100%),
    radial-gradient(ellipse 260px 60px at 300px 200px,rgba(230,230,230,.55),rgba(230,230,230,0)),
    radial-gradient(ellipse 200px 140px at 560px 260px,rgba(170,170,170,.45),rgba(170,170,170,0)),
    radial-gradient(ellipse 240px 120px at 120px 180px,rgba(150,150,150,.4),rgba(150,150,150,0)),
    linear-gradient(180deg,#111 0%,#2a2a2a 30%,#4a4a4a 60%,#6a6a6a 100%)}

.top-contact{position:absolute;right:140px;top:10px;font-size:7.5px;line-height:10px;color:var(--white);white-space:nowrap}
.social-top{position:absolute;left:570px;top:11px;display:flex;gap:9px}
.social-top span{width:13px;height:13px;border-radius:50%;background:var(--white);display:block}

.brand{position:absolute;left:42px;top:18px;display:flex;align-items:center;gap:8px}
.brand-mark{width:26px;height:26px;background:var(--orange)}
.brand-name{font-size:15px;font-weight:700;letter-spacing:2px;color:var(--white)}

.nav{position:absolute;left:0;top:75px;width:700px;height:33px;background:var(--nav)}
.nav ul{list-style:none;position:absolute;right:44px;top:11px;display:flex;gap:29px}
.nav li{font-size:9px;font-weight:700;color:var(--white)}

.hero-title{position:absolute;left:97px;top:288px;font-size:19px;line-height:21px;font-weight:800;color:var(--white);letter-spacing:-.2px}
.hero-lede{position:absolute;left:97px;top:334px;width:385px;font-size:8.4px;line-height:13px;font-weight:700;color:var(--white);text-transform:uppercase;letter-spacing:-.1px}
.btn-about{position:absolute;left:206px;top:409px;width:67px;height:22px;border:1px solid #666;font-size:8.5px;color:#555;display:flex;align-items:center;justify-content:center;background:#fff}

.intro-title{position:absolute;left:0;top:444px;width:700px;text-align:center;font-size:12px;font-weight:700;color:var(--ink)}
.intro-text{position:absolute;left:180px;top:473px;width:340px;text-align:center;font-size:8.5px;line-height:14px;color:var(--text)}

.persona-hex{position:absolute;width:146px;height:168px}
.persona-title{position:absolute;font-size:11.5px;line-height:11px;font-weight:700;color:var(--ink);text-transform:uppercase}
.persona-text{position:absolute;width:122px;font-size:7.6px;line-height:13.1px;color:var(--text);hyphens:auto;-webkit-hyphens:auto}

.footer{position:absolute;left:0;top:1003px;width:700px;height:197px;background:var(--footer);border-top:2px solid #d9d9d9}
.footer-badge{position:absolute;left:321px;top:-16px;width:58px;height:30px;background:var(--footer);display:flex;align-items:center;justify-content:center;font-size:9px;font-weight:700;color:var(--orange);letter-spacing:1px}
.footer-col{position:absolute;top:26px;width:145px}
.footer-col h3{font-size:8.5px;font-weight:700;color:var(--white);margin-bottom:12px}
.news-item{border-bottom:1px solid var(--footer-line);padding-bottom:12px;margin-bottom:12px}
.news-item:last-child{border:0}
.news-date{font-size:6.5px;color:#777;margin-bottom:3px}
.news-text{font-size:8px;line-height:11px;color:#ddd}
.contact-item{display:flex;gap:10px;margin-bottom:13px;align-items:flex-start}
.contact-icon{width:18px;height:18px;flex:none;border-radius:50%;background:#3a3a3a;display:flex;align-items:center;justify-content:center;margin-top:2px}
.contact-text{font-size:7.6px;line-height:11px;color:#ddd}
.footer-base{position:absolute;left:0;top:170px;width:700px;height:27px;background:var(--footer-base)}
.copyright{position:absolute;left:42px;top:9px;font-size:7.5px;color:#888}
.social-foot{position:absolute;right:42px;top:9px;display:flex;gap:6px}
.social-foot span{width:9px;height:9px;border-radius:50%;background:#777;display:block}
</style>
</head>
<body>

<div class="hero-photo" role="img" aria-label="Night aerial photograph of the London skyline with a lit bridge over the river"></div>

<div class="brand"><span class="brand-mark"></span><span class="brand-name">VELTRA</span></div>
<div class="top-contact">T: +44 20 7946 0960<br>E: INFO@VELTRA-EXAMPLE.CO.UK</div>
<div class="social-top" aria-label="Social links"><span></span><span></span><span></span><span></span></div>

<nav class="nav"><ul><li>ABOUT</li><li>SERVICES</li><li>PARTNERS</li><li>CLIENTS</li><li>CONTACT</li></ul></nav>

<h1 class="hero-title">YOU NEED INTEGRATION. WE’RE<br>ALWAYS THERE WITH YOU.</h1>
<p class="hero-lede">Veltra is one of the leading systems integrators to the world’s finance sector. We are an extension of your business and our services portfolio has been built so you always have access to a complete partner.</p>
<div class="btn-about">ABOUT US</div>

<h2 class="intro-title">WHO ARE YOU?</h2>
<p class="intro-text">If you’re part of a financial organisation, we have the power to help everyone work more efficiently, productively and profitably.</p>

<svg width="0" height="0" style="position:absolute">
  <defs>
    <linearGradient id="hexOrange" x1="0" y1="0" x2="1" y2="1">
      <stop offset="0" stop-color="#f7941d"/><stop offset="1" stop-color="#e2581a"/>
    </linearGradient>
    <linearGradient id="hexPhoto" x1="0" y1="0" x2="0" y2="1">
      <stop offset="0" stop-color="#e6e6e6"/><stop offset=".35" stop-color="#bdbdbd"/><stop offset=".6" stop-color="#4a4d57"/><stop offset="1" stop-color="#24262d"/>
    </linearGradient>
  </defs>
</svg>

<svg class="persona-hex" style="left:40px;top:476px" viewBox="0 0 146 168">
  <polygon points="73,0 146,42 146,126 73,168 0,126 0,42" fill="url(#hexOrange)"/>
  <polygon points="73,16 132,50 132,118 73,152 14,118 14,50" fill="#fff"/>
  <polygon role="img" aria-label="Portrait of a senior executive with folded arms" points="73,22 126,53 126,115 73,146 20,115 20,53" fill="url(#hexPhoto)"/>
</svg>
<svg class="persona-hex" style="left:199px;top:566px" viewBox="0 0 146 168">
  <polygon points="73,0 146,42 146,126 73,168 0,126 0,42" fill="url(#hexOrange)"/>
  <polygon points="73,16 132,50 132,118 73,152 14,118 14,50" fill="#fff"/>
  <polygon role="img" aria-label="Portrait of a finance director in a suit" points="73,22 126,53 126,115 73,146 20,115 20,53" fill="url(#hexPhoto)"/>
</svg>
<svg class="persona-hex" style="left:357px;top:566px" viewBox="0 0 146 168">
  <polygon points="73,0 146,42 146,126 73,168 0,126 0,42" fill="url(#hexOrange)"/>
  <polygon points="73,16 132,50 132,118 73,152 14,118 14,50" fill="#fff"/>
  <polygon role="img" aria-label="Portrait of an IT manager in a suit" points="73,22 126,53 126,115 73,146 20,115 20,53" fill="url(#hexPhoto)"/>
</svg>
<svg class="persona-hex" style="left:514px;top:476px" viewBox="0 0 146 168">
  <polygon points="73,0 146,42 146,126 73,168 0,126 0,42" fill="url(#hexOrange)"/>
  <polygon points="73,16 132,50 132,118 73,152 14,118 14,50" fill="#fff"/>
  <polygon role="img" aria-label="Portrait of an employee in business attire" points="73,22 126,53 126,115 73,146 20,115 20,53" fill="url(#hexPhoto)"/>
</svg>

<h3 class="persona-title" style="left:52px;top:655px">Senior<br>Hedge Fund<br>Manager/CEO</h3>
<p class="persona-text" style="left:52px;top:698px">You need to develop and implement strategies for business growth, while ensuring profitability. You’re aware your biggest asset is your staff and a happy workforce is a productive one. Security is a key concern in a changing always-on world and you need to be compliant, but you don’t want to overspend. Veltra can help you find the best solutions to help your business grow at the speed you want it to.</p>

<h3 class="persona-title" style="left:211px;top:744px">CFO</h3>
<p class="persona-text" style="left:211px;top:767px">Your key responsibility is to obtain the maximum ROI from products and services. You understand investment opportunities, providing they return higher efficiencies and revenues. You are concerned more with long-term spending versus short-term and how you can get the most value out of a proposition. Veltra can advise how to boost ROI by streamlining your business to maximise return.</p>

<h3 class="persona-title" style="left:368px;top:744px">IT Manager/CTO</h3>
<p class="persona-text" style="left:367px;top:767px">Integration with partners and services is your key concern. You want to make sure any IT system you implement will work with the whole infrastructure of your company. You don’t want your team to waste valuable time dealing with things that don’t matter. Veltra provides the whole picture to ensure your company is ready for the next generation of IT.</p>

<h3 class="persona-title" style="left:525px;top:653px">Employees</h3>
<p class="persona-text" style="left:525px;top:676px">You’re working hard, but not getting anywhere fast. You want the tools to make your job easier so you can spend more time thinking about what you’re doing rather than how you’re doing it. You shouldn’t have to think about the technology you’re using, because it should just work. Veltra can help you get back on track everyday.</p>

<footer class="footer">
  <div class="footer-badge">VELTRA</div>

  <div class="footer-col" style="left:42px">
    <h3>RECENT NEWS</h3>
    <div class="news-item"><div class="news-date">10 MAR 2015</div><div class="news-text">Mirum est notare quam littera gothica, quam nunc</div></div>
    <div class="news-item"><div class="news-date">10 MAR 2015</div><div class="news-text">Mirum est notare quam littera gothica, quam nunc</div></div>
  </div>

  <div class="footer-col" style="left:200px">
    <h3>RECENT BLOG</h3>
    <div class="news-item"><div class="news-date">10 MAR 2015 | 10 COMMENTS</div><div class="news-text">Mirum est notare quam littera gothica, quam nunc</div></div>
    <div class="news-item"><div class="news-date">10 MAR 2015 | 10 COMMENTS</div><div class="news-text">Mirum est notare quam littera gothica, quam nunc</div></div>
  </div>

  <div class="footer-col" style="left:358px">
    <h3>LONDON OFFICE</h3>
    <div class="contact-item"><span class="contact-icon"><svg width="8" height="10" viewBox="0 0 8 10"><path d="M4 0a4 4 0 0 1 4 4c0 3-4 6-4 6S0 7 0 4a4 4 0 0 1 4-4z" fill="#fff"/><circle cx="4" cy="4" r="1.4" fill="#3a3a3a"/></svg></span><span class="contact-text">12 Harlow Street,<br>Mayfair, London W1K 0AA</span></div>
    <div class="contact-item"><span class="contact-icon"><svg width="9" height="9" viewBox="0 0 10 10"><path d="M2 0l2 2.5-1.2 1.2a6 6 0 0 0 3.5 3.5L7.5 6 10 8l-1.5 2C4 10 0 6 0 1.5z" fill="#fff"/></svg></span><span class="contact-text">Phone :<br>+44 20 7946 0961</span></div>
    <div class="contact-item"><span class="contact-icon"><svg width="9" height="7" viewBox="0 0 10 7"><rect width="10" height="7" fill="#fff"/><path d="M0 0l5 4 5-4" fill="none" stroke="#3a3a3a" stroke-width="1"/></svg></span><span class="contact-text">Email :<br>info@veltra-example.co.uk</span></div>
  </div>

  <div class="footer-col" style="left:515px">
    <h3>ESSEX OFFICE</h3>
    <div class="contact-item"><span class="contact-icon"><svg width="8" height="10" viewBox="0 0 8 10"><path d="M4 0a4 4 0 0 1 4 4c0 3-4 6-4 6S0 7 0 4a4 4 0 0 1 4-4z" fill="#fff"/><circle cx="4" cy="4" r="1.4" fill="#3a3a3a"/></svg></span><span class="contact-text">8 Mill Works, Mill Lane<br>Southend, Essex SS0 0AA</span></div>
    <div class="contact-item"><span class="contact-icon"><svg width="9" height="9" viewBox="0 0 10 10"><path d="M2 0l2 2.5-1.2 1.2a6 6 0 0 0 3.5 3.5L7.5 6 10 8l-1.5 2C4 10 0 6 0 1.5z" fill="#fff"/></svg></span><span class="contact-text">Phone :<br>+44 20 7946 0960</span></div>
    <div class="contact-item"><span class="contact-icon"><svg width="9" height="7" viewBox="0 0 10 7"><rect width="10" height="7" fill="#fff"/><path d="M0 0l5 4 5-4" fill="none" stroke="#3a3a3a" stroke-width="1"/></svg></span><span class="contact-text">Email :<br>info@veltra-example.co.uk</span></div>
  </div>

  <div class="footer-base">
    <div class="copyright">© 2015 Veltra Limited. All Rights Reserved.</div>
    <div class="social-foot" aria-label="Social links"><span></span><span></span><span></span><span></span></div>
  </div>
</footer>

</body>
</html>
```